Family Ranch with a hobby vineyard needs 2 wine labels for our first harvest

Design 2 wine labels (front and back) with the Brindor Ranch logo.
Label 1:
Sauvignon Blanc
Alc. 12.5% by Vol.
Palos Verdes Peninsula - add as the region
Year 2022
Label 2:
Cabernet Sauvignon
Alc. 13.5% by Vol.
Year 2022
For the back label design:
GOVERNMENT WARNING: (1) According to the Surgeon General, women
should not drink alcoholic beverages during pregnancy because of the risk of
birth defects. (2) Consumption of alcoholic beverages impairs your ability to
drive a car or operate machinery, and may cause health problems.
Contains Sulfates.
750ML
I just received the bottles and have attached a picture.
Look and feel
Each slider illustrates characteristics of the customer's brand and the style your logo design should communicate.

```html
<!DOCTYPE html>
<html lang="en">
<head>
<meta charset="utf-8">
<title>Brindor Ranch Wine Labels</title>
<link rel="stylesheet" href="https://fonts.googleapis.com/css2?family=Josefin+Sans:wght@600;700&display=swap">
<style>
  :root {
    --page: #ffffff;
    --label-bg: #c6c7cc;
    --leaf-tone: #d6d7db;
    --arch-tone: #eeeff1;
    --ink: #4f5156;
    --ink-dark: #2c2d31;
    --white-wine: #e6d386;
    --white-band: #e8d67a;
    --red-wine: #7e1a38;
    --red-band: #8a1f3f;
  }
  * { margin: 0; padding: 0; box-sizing: border-box; }
  html, body {
    width: 1200px; height: 1200px; overflow: hidden;
    background: var(--page);
  }
  .canvas {
    position: relative; width: 1200px; height: 1200px;
    display: flex; justify-content: center; align-items: center; gap: 80px;
  }
  .wine-label {
    width: 480px; height: 644px; display: block;
    box-shadow: 0 6px 24px rgba(0,0,0,0.12);
  }
  .label-text {
    font-family: "Josefin Sans", sans-serif;
    font-variant: small-caps;
    font-weight: 700;
    fill: var(--ink);
  }
  .varietal { font-size: 23px; }
  .vintage { font-size: 14px; fill: var(--ink-dark); }
  .detail { font-size: 11px; }
  .brand-name { font-size: 15px; fill: var(--ink-dark); }
</style>
</head>
<body>
<main class="canvas">

  <svg class="wine-label label-sauvignon-blanc" viewBox="0 0 410 550" aria-label="Sauvignon Blanc label">
    <defs>
      <linearGradient id="leavesBlanc" x1="0" y1="0" x2="0" y2="1">
        <stop offset="0" stop-color="var(--leaf-tone)"/>
        <stop offset="1" stop-color="var(--label-bg)" stop-opacity="0"/>
      </linearGradient>
      <linearGradient id="artBlanc" x1="0" y1="0" x2="0" y2="1">
        <stop offset="0" stop-color="var(--arch-tone)"/>
        <stop offset="0.35" stop-color="var(--arch-tone)"/>
        <stop offset="1" stop-color="var(--white-wine)"/>
      </linearGradient>
    </defs>
    <rect class="label-ground" width="410" height="550" fill="var(--label-bg)"/>
    <rect class="leaf-artwork" role="img" aria-label="Faint grape vine leaves along the top edge" width="410" height="170" fill="url(#leavesBlanc)"/>
    <rect class="hero-artwork" role="img" aria-label="Illustration of white wine in a glass framed by a pale arch" x="22" y="45" width="366" height="315" rx="40" fill="url(#artBlanc)" opacity="0.85"/>
    <text class="label-text varietal" x="205" y="110" text-anchor="middle">Sauvignon</text>
    <text class="label-text varietal" x="205" y="134" text-anchor="middle">Blanc</text>
    <text class="label-text vintage" x="205" y="413" text-anchor="middle">Year</text>
    <text class="label-text vintage" x="205" y="430" text-anchor="middle">2022</text>
    <circle class="brand-dot" cx="205" cy="478" r="13" fill="var(--ink-dark)"/>
    <text class="label-text brand-name" x="205" y="512" text-anchor="middle">Brindor Ranch</text>
    <text class="label-text detail" x="95" y="502" text-anchor="middle">Alc. 12.5%</text>
    <text class="label-text detail" x="88" y="515" text-anchor="middle">by Vol.</text>
    <text class="label-text detail" x="313" y="502" text-anchor="middle">Palos Verdes</text>
    <text class="label-text detail" x="305" y="515" text-anchor="middle">Peninsula</text>
    <rect class="base-band" y="540" width="410" height="10" fill="var(--white-band)"/>
  </svg>

  <svg class="wine-label label-cabernet" viewBox="0 0 410 550" aria-label="Cabernet Sauvignon label">
    <defs>
      <linearGradient id="leavesCab" x1="0" y1="0" x2="0" y2="1">
        <stop offset="0" stop-color="var(--leaf-tone)"/>
        <stop offset="1" stop-color="var(--label-bg)" stop-opacity="0"/>
      </linearGradient>
      <linearGradient id="artCab" x1="0" y1="0" x2="0" y2="1">
        <stop offset="0" stop-color="var(--arch-tone)"/>
        <stop offset="0.35" stop-color="var(--arch-tone)"/>
        <stop offset="1" stop-color="var(--red-wine)"/>
      </linearGradient>
    </defs>
    <rect class="label-ground" width="410" height="550" fill="var(--label-bg)"/>
    <rect class="leaf-artwork" role="img" aria-label="Faint grape vine leaves along the top edge" width="410" height="170" fill="url(#leavesCab)"/>
    <rect class="hero-artwork" role="img" aria-label="Illustration of red wine in a glass framed by a pale arch" x="22" y="45" width="366" height="315" rx="40" fill="url(#artCab)" opacity="0.85"/>
    <text class="label-text varietal" x="205" y="110" text-anchor="middle">Cabernet</text>
    <text class="label-text varietal" x="205" y="134" text-anchor="middle">Sauvignon</text>
    <text class="label-text vintage" x="205" y="413" text-anchor="middle">Year</text>
    <text class="label-text vintage" x="205" y="430" text-anchor="middle">2022</text>
    <circle class="brand-dot" cx="205" cy="478" r="13" fill="var(--ink-dark)"/>
    <text class="label-text brand-name" x="205" y="512" text-anchor="middle">Brindor Ranch</text>
    <text class="label-text detail" x="95" y="502" text-anchor="middle">Alc. 13.5%</text>
    <text class="label-text detail" x="88" y="515" text-anchor="middle">by Vol.</text>
    <text class="label-text detail" x="313" y="502" text-anchor="middle">Palos Verdes</text>
    <text class="label-text detail" x="305" y="515" text-anchor="middle">Peninsula</text>
    <rect class="base-band" y="540" width="410" height="10" fill="var(--red-band)"/>
  </svg>

</main>
</body>
</html>
```